Website Home Page for Women's Health Medical Office

Redesign existing homepage for website using existing logo. Current website location is www.larkfieldwomenscare.com. Please give it a modern, streamlined, playful feel.

Please give it a feminine feel and make it bright and cheerful using logo colors.

Target Market(s)

Women between the ages of 25-45

Industry/Entity Type

Medical Office

Coding

Coded - Design and coding required

Number of Pages Required

1 page

Font styles to use
Sans Serif
Other font styles liked:
• SEGOI UI script for text and GIL SANS for bold (or their equivilent)

Colors
E54698
E96AAD
F1A4CE
F9D9EA
FCEFF6

Requirements
Must have
• Existing logo. Logo Colors. Feminine, cheerful, simple design. all relevant contact information
Nice to have
• clean lines and streamlined look
Should not have
• Cluttered

```html
<!DOCTYPE html>
<html lang="en">
<head>
<meta charset="utf-8">
<title>Larkfield Women's Care</title>
<link href="https://fonts.googleapis.com/css2?family=Cabin:wght@400;500;600;700&display=swap" rel="stylesheet">
<style>
:root{
  --pink:#e54698;
  --pink-mid:#e96aad;
  --pink-soft:#f1a4ce;
  --pink-pale:#f9d9ea;
  --pink-mist:#fceff6;
  --berry:#9c1660;
  --ink:#111111;
  --grey-btn:#bdbdbd;
  --white:#ffffff;
}
*{margin:0;padding:0;box-sizing:border-box}
html,body{width:1200px;height:675px;overflow:hidden;background:var(--white)}
body{font-family:"Cabin",sans-serif;color:var(--ink);position:relative}
.hero-art{position:absolute;left:0;top:0;width:1200px;height:675px}
.topbar{position:absolute;left:0;top:0;width:1200px;height:34px;background:linear-gradient(180deg,var(--pink) 0%,#b82a74 100%);color:var(--white);font-size:11.5px;display:flex;align-items:center;justify-content:space-between;padding:0 78px 0 105px}
.topbar .group{display:flex;gap:32px;align-items:center}
.topbar .item{display:flex;align-items:center;gap:10px}
.topbar .item a{color:var(--white)}
.topbar svg{width:15px;height:15px;fill:var(--white)}
.nav{position:absolute;top:118px;display:flex;gap:4px}
.nav-left{left:117px}
.nav-right{left:757px}
.nav a{display:flex;align-items:center;justify-content:center;width:110px;height:32px;border-radius:3px;font-size:11.5px;color:var(--white);text-decoration:none;background:var(--grey-btn)}
.nav a.active{background:var(--pink);font-weight:700;font-size:12.5px}
.nav-right a{background:rgba(140,140,140,.45)}
.brand{position:absolute;left:450px;top:160px;width:300px;display:flex;align-items:center;justify-content:center;gap:9px}
.brand .dot{width:14px;height:14px;border-radius:50%;background:var(--pink)}
.brand .name{font-size:22px;font-weight:700;color:#3a3a3a}
.headline{position:absolute;left:296px;top:272px;font-size:51px;font-weight:700;line-height:69px;letter-spacing:-.3px}
.hero-copy{position:absolute;left:296px;top:412px;width:415px;font-size:7px;line-height:9.5px;text-align:justify}
.cta{position:absolute;left:296px;top:439px;width:151px;height:30px;background:var(--pink-soft);border-radius:3px;display:flex;align-items:center;justify-content:space-between;padding:0 16px;font-size:12px;font-weight:700;color:var(--ink);text-decoration:none}
.cta svg{width:15px;height:16px}
.welcome{position:absolute;left:551px;top:623px;font-size:30px;font-weight:700;color:var(--berry);letter-spacing:.2px}
</style>
</head>
<body>
<svg class="hero-art" viewBox="0 0 1200 675" aria-hidden="false">
  <defs>
    <linearGradient id="photoTone" x1="0" y1="0" x2="1" y2="0">
      <stop offset="0" stop-color="#ffffff"/>
      <stop offset=".38" stop-color="#f6f4f3"/>
      <stop offset=".6" stop-color="#dcd5d1"/>
      <stop offset=".78" stop-color="#b9b4b3"/>
      <stop offset=".9" stop-color="#5f7f66"/>
      <stop offset="1" stop-color="#3f6a4f"/>
    </linearGradient>
  </defs>
  <rect x="0" y="34" width="1200" height="560" fill="url(#photoTone)" role="img" aria-label="Photo of an expectant mother in a bright room with houseplants"/>
  <path d="M0 520 C90 500 180 480 300 488 C450 500 640 570 880 603 C1000 618 1120 612 1200 580 L1200 675 L0 675 Z" fill="#ffffff"/>
  <path d="M36 598 C36 540 60 520 90 555 C130 600 170 640 210 650 L360 650 C390 610 410 560 440 548 C470 536 490 590 493 675 L36 675 Z" fill="var(--pink)"/>
  <rect x="150" y="505" width="240" height="170" rx="90" fill="var(--pink-pale)" role="img" aria-label="Portrait photo of a smiling doctor in a white coat"/>
</svg>

<header class="topbar">
  <div class="group">
    <span class="item"><svg viewBox="0 0 24 24"><path d="M6.6 10.8a15.1 15.1 0 0 0 6.6 6.6l2.2-2.2c.3-.3.7-.4 1-.2 1.1.4 2.3.6 3.6.6.6 0 1 .4 1 1V20c0 .6-.4 1-1 1A17 17 0 0 1 3 4c0-.6.4-1 1-1h3.5c.6 0 1 .4 1 1 0 1.3.2 2.5.6 3.6.1.3 0 .7-.2 1z"/></svg><a href="#">(555) 014-2387</a></span>
    <span class="item"><svg viewBox="0 0 24 24"><path d="M2 5h20v2l-10 6L2 7zM2 9l10 6 10-6v10H2z"/></svg>admin@larkfieldwomenscare.com</span>
  </div>
  <div class="group">
    <span class="item"><svg viewBox="0 0 24 24"><path d="M12 2a7 7 0 0 0-7 7c0 5 7 13 7 13s7-8 7-13a7 7 0 0 0-7-7zm0 9.5A2.5 2.5 0 1 1 12 6.5a2.5 2.5 0 0 1 0 5z"/></svg>1480 Meadowlark Road, Suite 120, Larkfield, CA 90210</span>
    <span class="item"><svg viewBox="0 0 24 24"><path d="M6.6 10.8a15.1 15.1 0 0 0 6.6 6.6l2.2-2.2c.3-.3.7-.4 1-.2 1.1.4 2.3.6 3.6.6.6 0 1 .4 1 1V20c0 .6-.4 1-1 1A17 17 0 0 1 3 4c0-.6.4-1 1-1h3.5c.6 0 1 .4 1 1 0 1.3.2 2.5.6 3.6.1.3 0 .7-.2 1z"/></svg>555-014-2391</span>
  </div>
</header>

<nav class="nav nav-left">
  <a class="active" href="#">Home</a>
  <a href="#">Service</a>
  <a href="#">Resource</a>
</nav>
<nav class="nav nav-right">
  <a href="#">About Us</a>
  <a href="#">Contact Us</a>
  <a href="#">Contact Us</a>
</nav>

<div class="brand"><span class="dot"></span><span class="name">Larkfield Women's Care</span></div>

<h1 class="headline">Lorem Ipsum is<br>simply dummy</h1>
<p class="hero-copy">Lorem Ipsum is simply dummy text of the printing and typesetting industry. Lorem Ipsum has been the industry's standard dummy text ever since the 1500s, when an unknown printer took a galley of type and scrambled it to make a type specimen book. It has survived not only five centuries.</p>
<a class="cta" href="#">Appointment
  <svg viewBox="0 0 16 17"><rect x="1" y="3" width="14" height="13" rx="1.5" fill="#111"/><rect x="4" y="1" width="2" height="4" fill="#111"/><rect x="10" y="1" width="2" height="4" fill="#111"/><rect x="2.5" y="6" width="11" height="1" fill="#fff"/><path d="M5 11l2 2 4-4" stroke="#fff" stroke-width="1.6" fill="none"/></svg>
</a>

<h2 class="welcome">WELCOME TO LARKFIELD WOMEN'S CARE,</h2>
</body>
</html>
```